Web Design Project (uncoded)

About Us
ZumLink is a telecom startup and is looking to launch its website.
ZumLink specializes in providing communication solutions to the travel market. Our mission is to develop cost effective communication products and solutions for the international traveler.
Our simple vision of "every hotel should have a mobile phone in the guest rooms", led us to develop a pathbreaking & cost effective mobile phone. With full integration capabilities with the hotels property management system, location based marketing, user locator and other features, this product is unique in addressing the hospitality segment.
The website is targeted at hotel owners and property management companies.
The website should have a young contemporary and a funky look, in line with the name.
Please find attached our logo (for the colors etc.). (attached now).
We would like to receive the design for a home page and an inside page for the website.
Site map would be as follows: Home, About Us, Solutions, Contact us
Thanks and look forward,
Tamsa
Target Market(s)
Hotel decision makers
Industry/Entity Type
Property Management
Look and feel
Each slider illustrates characteristics of the customer's brand and the style your logo design should communicate.

```html
<!DOCTYPE html>
<html lang="en">
<head>
<meta charset="utf-8">
<title>ZumLink – Home</title>
<link rel="stylesheet" href="https://fonts.googleapis.com/css2?family=Arimo:wght@400;700&family=Mulish:wght@400;600;700;800&family=Didact+Gothic&display=swap">
<style>
:root{
  --page:#f6f6f6;
  --ink:#333333;
  --heading:#666666;
  --muted:#8a8a8a;
  --orange:#f08a12;
  --orange-light:#f7a534;
  --yellow:#f2b321;
  --yellow-light:#f6c540;
  --line:#d8d8d8;
  --white:#ffffff;
}
*{margin:0;padding:0;box-sizing:border-box}
html,body{width:1200px;height:900px;overflow:hidden}
body{background:var(--page);font-family:"Arimo",Arial,sans-serif;color:var(--ink);position:relative}
.abs{position:absolute}

/* Header */
.site-header{position:absolute;left:0;top:0;width:1200px;height:163px;background:linear-gradient(#ffffff,#efefef)}
.brand{left:143px;top:52px;display:flex;align-items:center;gap:14px}
.brand-dot{width:100px;height:100px;border-radius:50%;background:var(--orange)}
.brand-name{font-family:"Mulish",sans-serif;font-weight:800;font-size:56px;color:#222;letter-spacing:-1px}
.support-photo{left:745px;top:8px;width:92px;height:112px;background:linear-gradient(#e9e4df,#cfc7c0);border-radius:40px 40px 0 0}
.account-links{left:848px;top:27px;font-family:"Arimo",sans-serif;font-weight:700;font-size:13px;color:#777;word-spacing:2px}
.account-links span.sep{color:#aaa;margin:0 14px;font-weight:400}
.support-note{left:849px;top:64px;font-family:"Didact Gothic",sans-serif;font-size:14.5px;color:#555}
.support-phone{left:849px;top:84px;font-family:"Didact Gothic",sans-serif;font-size:20px;color:var(--orange)}
.main-nav{left:505px;top:118px;width:574px;height:46px;background:linear-gradient(#ffffff,#eef0f2);border:1px solid #d6dadf;border-bottom:none;border-radius:6px 6px 0 0}
.main-nav a{position:absolute;top:15px;font-family:"Mulish",sans-serif;font-weight:700;font-size:16px;color:#6a6a6a;text-decoration:none;letter-spacing:1px}

/* Hero */
.hero-band{left:0;top:163px;width:1200px;height:394px;background:linear-gradient(var(--yellow-light),var(--yellow))}
.hero-shadow{left:130px;top:522px;width:940px;height:24px;border-radius:50%;background:rgba(120,70,0,.35);filter:blur(8px)}
.hero{left:110px;top:192px;width:980px;height:336px;overflow:hidden}
.hero-photo-left{left:0;top:0;width:482px;height:336px;background:linear-gradient(120deg,#c88a2c,#e8b25a 45%,#b07a3c)}
.hero-divider{left:482px;top:0;width:8px;height:336px;background:var(--orange-light)}
.hero-photo-right{left:490px;top:0;width:490px;height:336px;background:linear-gradient(120deg,#d9d3cc,#f0eeec 55%,#c9c2ba)}
.hero-badge{left:430px;top:110px;width:112px;height:112px;border-radius:50%;background:#1f1f1f;border:7px solid var(--orange-light)}
.hero-caption{left:0;top:257px;width:980px;height:79px;background:rgba(255,255,255,.62)}
.hero-caption p{position:absolute;left:45px;top:26px;font-family:"Mulish",sans-serif;font-weight:700;font-size:20px;color:#2b2b2b}
.read-more{left:748px;top:14px}
.read-more span{position:absolute;left:34px;top:15px;font-family:"Mulish",sans-serif;font-weight:700;font-size:18px;color:#3b2a10}

/* Content */
.section-icon{border-radius:6px}
.section-title{font-family:"Mulish",sans-serif;font-weight:800;font-size:20px;color:var(--heading)}
.dots{height:0;border-top:3px dotted #cfcfcf}
.reasons{left:140px;top:650px;list-style:none}
.reasons li{height:30px;font-size:12px;color:var(--muted);padding-left:26px;position:relative}
.reasons li svg{position:absolute;left:0;top:0}
.testimonial{left:821px;top:591px;width:250px;height:230px;border:1px solid #dcdcdc;background:linear-gradient(#ffffff,#ececec)}
.testimonial h3{position:absolute;left:29px;top:12px;font-family:"Mulish",sans-serif;font-weight:800;font-size:18px;color:var(--orange)}
.testimonial p{position:absolute;left:30px;top:50px;width:208px;font-size:12px;line-height:20px;color:var(--muted)}
.testimonial-tail{left:989px;top:819px}
.client-photo{left:824px;top:829px;width:59px;height:59px;border:3px solid #e2e2e2;background:linear-gradient(#8a5a44,#c99a80)}
.client-name{left:896px;top:845px;font-weight:700;font-size:12px;color:#555}
.client-role{left:896px;top:863px;font-weight:700;font-size:12px;color:#888}
.about-text{left:120px;top:893px;font-size:12px;color:#888;white-space:nowrap}
</style>
</head>
<body>

<header class="site-header">
  <div class="abs brand"><span class="brand-dot"></span><span class="brand-name">ZumLink</span></div>
  <div class="abs support-photo" role="img" aria-label="Photo of a customer support agent wearing a headset"></div>
  <div class="abs account-links">My Account<span class="sep">|</span>Login<span class="sep">|</span>Help</div>
  <div class="abs support-note">24x7 Online customer support</div>
  <div class="abs support-phone">Call us: 1300 555 0142</div>
  <nav class="abs main-nav">
    <a href="#" style="left:59px">HOME</a>
    <a href="#" style="left:141px">ABOUT US</a>
    <a href="#" style="left:251px">SOLUTIONS</a>
    <a href="#" style="left:371px">CONTACT US</a>
  </nav>
</header>

<section class="abs hero-band">
</section>
<div class="abs hero-shadow"></div>
<div class="abs hero">
  <div class="abs hero-photo-left" role="img" aria-label="Photo of a smiling woman texting on a mobile phone in a hotel bed"></div>
  <div class="abs hero-divider"></div>
  <div class="abs hero-photo-right" role="img" aria-label="Photo of a man reading his mobile phone in a hotel bed"></div>
  <div class="abs hero-badge"></div>
  <div class="abs hero-caption">
    <p>Keeping in touch with family, friends and work has never been so easy</p>
    <a class="abs read-more" href="#">
      <svg width="172" height="53" viewBox="0 0 172 53"><defs><linearGradient id="btn" x1="0" y1="0" x2="0" y2="1"><stop offset="0" stop-color="#fbb040"/><stop offset="1" stop-color="#ee7d0c"/></linearGradient></defs><path d="M2 1H148L171 26.5L148 52H2L10 26.5Z" fill="url(#btn)" stroke="#d9700a"/></svg>
      <span>Read More</span>
    </a>
  </div>
</div>

<div class="abs section-icon" style="left:118px;top:576px;width:68px;height:58px;background:linear-gradient(#f2efe6,#cfc8b8)" role="img" aria-label="Illustration of a notepad with a magnifying glass"></div>
<h2 class="abs section-title" style="left:193px;top:585px">Why Choose US?</h2>
<div class="abs dots" style="left:197px;top:613px;width:601px"></div>
<ul class="abs reasons">
  <li><svg width="16" height="16" viewBox="0 0 16 16"><path d="M2 2l8 8V5h3v10H3v-3h5L0 4z" fill="#aaa"/></svg>Lorem ipsum dolor sit amet, consectetur adipisicing elit.</li>
  <li><svg width="16" height="16" viewBox="0 0 16 16"><path d="M2 2l8 8V5h3v10H3v-3h5L0 4z" fill="#aaa"/></svg>Sed do eiusmod tempor incididunt ut labore et dolore magna aliqua.</li>
  <li><svg width="16" height="16" viewBox="0 0 16 16"><path d="M2 2l8 8V5h3v10H3v-3h5L0 4z" fill="#aaa"/></svg>Lorem ipsum dolor quis nostrud exercitation ullamco laboris nisi ut aliquip ex</li>
  <li><svg width="16" height="16" viewBox="0 0 16 16"><path d="M2 2l8 8V5h3v10H3v-3h5L0 4z" fill="#aaa"/></svg>Lorem ipsum dolor sit amet, consectetur adipisicing elit</li>
  <li><svg width="16" height="16" viewBox="0 0 16 16"><path d="M2 2l8 8V5h3v10H3v-3h5L0 4z" fill="#aaa"/></svg>Ut enim ad minim veniam, quis nostrud exercitation ullamco laboris nisi ut</li>
</ul>

<aside class="abs testimonial">
  <h3>What our clients say</h3>
  <p>Lorem ipsum dolor sit amet, consectetur adipisicing elit, sed do eiusmod tempor incididunt ut labore et dolore magna aliqua. Ut enim ad minim veniam, quis nostrud exercitation ullamco laboris nisi ut aliquip ex ea</p>
</aside>
<svg class="abs testimonial-tail" width="38" height="22" viewBox="0 0 38 22"><path d="M1 0L0 21L36 0" fill="#ececec" stroke="#dcdcdc"/><path d="M2 0H35" stroke="#ececec" stroke-width="2"/></svg>
<div class="abs client-photo" role="img" aria-label="Portrait photo of the client"></div>
<div class="abs client-name">Delara V</div>
<div class="abs client-role">Hotel Meridale CEO</div>

<div class="abs section-icon" style="left:117px;top:830px;width:62px;height:52px;background:linear-gradient(#b07a44,#6e4420)" role="img" aria-label="Illustration of a leather wallet"></div>
<h2 class="abs section-title" style="left:191px;top:843px">About US</h2>
<div class="abs dots" style="left:285px;top:868px;width:513px"></div>
<p class="abs about-text">Lorem ipsum dolor sit amet, consectetur adipisicing elit, sed do eiusmod tempor incididunt ut labore et dolore.</p>

</body>
</html>
```